Digital & Print Graphic Design templates for Comedy Club

We need new new digital & print graphic design templates for our upcoming comedy events created for use in CANVA in the following specs
Digital:
1080x1080px
1200x600px
800x400px
1920x1080px
1080x1355px
1500x500px
851x315px
Print
11x17"
22x28"
95.5x30"

Target Market(s)

18+ comedy fans

Industry/Entity Type

comedy club

Font styles to use
Sans Serif

Colors
FFF300
FFF600
FEFA6F
FFFEC7
FFFEE8
6B429C
8869AF
B7A5CE
E3DAEB
F3F0F8

Requirements
Must have
• templates must be CANVA compatible. frame for comedian photo.
Nice to have
• would like to incorporate deep purple into the design
Should not have
• do not include phone number on any templates

```html
<!DOCTYPE html>
<html lang="en">
<head>
<meta charset="utf-8">
<title>Dex Marlow – Live at Giggle Room</title>
<link rel="stylesheet" href="https://fonts.googleapis.com/css2?family=Montserrat:wght@600;700;800&display=swap">
<style>
  :root {
    --yellow: #FFF300;
    --yellow-deep: #C9B800;
    --yellow-soft: #FEFA6F;
    --cream: #FFFEC7;
    --white: #FFFFFF;
    --purple-night: #1E0846;
    --purple-deep: #35107A;
    --purple-brick: #4A1FA0;
    --lilac: #B7A5CE;
    --lilac-mid: #8869AF;
    --badge-black: #0B0B0B;
  }
  * { margin: 0; padding: 0; box-sizing: border-box; }
  html, body { width: 1200px; height: 1200px; overflow: hidden; }
  body { font-family: "Montserrat", sans-serif; background: var(--purple-night); }

  .poster {
    position: relative;
    width: 1200px;
    height: 1200px;
    overflow: hidden;
    background:
      radial-gradient(circle at 50% 45%, var(--purple-brick) 0%, var(--purple-deep) 55%, var(--purple-night) 100%);
  }
  .poster__wall {
    position: absolute; inset: 0;
  }
  .glow {
    position: absolute;
    width: 150px; height: 150px;
    border-radius: 50%;
    background: radial-gradient(circle, rgba(255,254,232,0.95) 0%, rgba(255,230,160,0.45) 18%, rgba(255,200,120,0.12) 45%, rgba(255,200,120,0) 70%);
  }
  .glow--left  { left: 61px;  top: 151px; }
  .glow--right { left: 1029px; top: 332px; }

  .kicker {
    position: absolute;
    top: 70px; left: 0; width: 100%;
    text-align: center;
    color: var(--white);
    font-weight: 700;
    font-size: 37px;
    letter-spacing: 0.5px;
  }

  .stage { position: absolute; left: 0; top: 0; width: 1200px; height: 1200px; }

  .club-badge {
    position: absolute;
    left: 121px; top: 563px;
    width: 214px; height: 214px;
    border-radius: 50%;
    background: var(--badge-black);
    border: 4px solid var(--yellow);
    display: flex; align-items: center; justify-content: center;
    text-align: center;
  }
  .club-badge__name {
    color: var(--yellow);
    font-weight: 800;
    font-size: 30px;
    line-height: 1.05;
    text-transform: uppercase;
  }

  .headliner { position: absolute; left: 0; top: 0; }

  .details {
    position: absolute;
    top: 1024px; left: 0; width: 100%;
    display: flex; justify-content: center; gap: 66px;
    color: var(--white);
    font-weight: 700;
    font-size: 30px;
  }
  .details__item { display: flex; align-items: center; gap: 20px; }
  .details__icon { width: 52px; height: 52px; flex: none; }

  .venue {
    position: absolute;
    top: 1102px; left: 0; width: 100%;
    display: flex; justify-content: center; align-items: center; gap: 26px;
    color: var(--white);
    font-weight: 700;
    font-size: 25px;
  }
  .venue__dot { width: 11px; height: 11px; border-radius: 50%; background: var(--white); }
</style>
</head>
<body>
<main class="poster">
  <div class="poster__wall" role="img" aria-label="Deep purple brick wall backdrop"></div>
  <span class="glow glow--left"></span>
  <span class="glow glow--right"></span>

  <p class="kicker">LIVE AT GIGGLE ROOM</p>

  <svg class="stage" viewBox="0 0 1200 1200" aria-hidden="false">
    <defs>
      <radialGradient id="bulb" cx="50%" cy="50%" r="50%">
        <stop offset="0%" stop-color="#FFFEE8"/>
        <stop offset="55%" stop-color="#FEFA6F"/>
        <stop offset="100%" stop-color="#F0B930"/>
      </radialGradient>
      <linearGradient id="photoFill" x1="0" y1="0" x2="0" y2="1">
        <stop offset="0%" stop-color="#2A0C66"/>
        <stop offset="100%" stop-color="#1A0840"/>
      </linearGradient>
    </defs>

    <!-- marquee ring -->
    <circle cx="585" cy="567" r="372" fill="none" stroke="#9C86CC" stroke-width="76" opacity="0.85"/>
    <circle cx="585" cy="567" r="413" fill="none" stroke="#FFFEC7" stroke-width="5"/>
    <circle cx="585" cy="567" r="332" fill="none" stroke="#FFFEC7" stroke-width="5"/>

    <!-- comedian photo frame -->
    <circle cx="585" cy="567" r="328" fill="url(#photoFill)" role="img" aria-label="Photo of the headlining comedian"/>

    <g class="marquee-bulbs" fill="url(#bulb)">
      <circle cx="955" cy="567" r="19"/><circle cx="937" cy="681" r="19"/>
      <circle cx="884" cy="785" r="19"/><circle cx="803" cy="866" r="19"/>
      <circle cx="699" cy="919" r="19"/><circle cx="585" cy="937" r="19"/>
      <circle cx="471" cy="919" r="19"/><circle cx="367" cy="866" r="19"/>
      <circle cx="286" cy="785" r="19"/><circle cx="233" cy="681" r="19"/>
      <circle cx="215" cy="567" r="19"/><circle cx="233" cy="453" r="19"/>
      <circle cx="286" cy="349" r="19"/><circle cx="367" cy="268" r="19"/>
      <circle cx="471" cy="215" r="19"/><circle cx="585" cy="197" r="19"/>
      <circle cx="699" cy="215" r="19"/><circle cx="803" cy="268" r="19"/>
      <circle cx="884" cy="349" r="19"/><circle cx="937" cy="453" r="19"/>
    </g>

    <!-- headliner name -->
    <g class="headliner" font-family="Montserrat, sans-serif" font-weight="700" font-size="180">
      <text x="72" y="980" textLength="1100" lengthAdjust="spacingAndGlyphs" fill="#6B5A00" opacity="0.75">DEX MARLOW</text>
      <text x="63" y="968" textLength="1100" lengthAdjust="spacingAndGlyphs" fill="#FFF300">DEX MARLOW</text>
    </g>
  </svg>

  <div class="club-badge">
    <span class="club-badge__name">The<br>Giggle<br>Room</span>
  </div>

  <div class="details">
    <div class="details__item">
      <svg class="details__icon" viewBox="0 0 52 52">
        <rect x="0" y="0" width="52" height="52" rx="6" fill="#FFF300"/>
        <rect x="9" y="11" width="34" height="32" rx="3" fill="none" stroke="#1E0846" stroke-width="3"/>
        <rect x="9" y="11" width="34" height="7" fill="#1E0846"/>
        <g fill="#1E0846">
          <rect x="14" y="22" width="5" height="5"/><rect x="23" y="22" width="5" height="5"/><rect x="32" y="22" width="5" height="5"/>
          <rect x="14" y="31" width="5" height="5"/><rect x="23" y="31" width="5" height="5"/><rect x="32" y="31" width="5" height="5"/>
        </g>
      </svg>
      <span>Wednesday 4 Feb, 2026</span>
    </div>
    <div class="details__item">
      <svg class="details__icon" viewBox="0 0 52 52">
        <rect x="0" y="0" width="52" height="52" rx="6" fill="#FFF300"/>
        <circle cx="26" cy="26" r="16" fill="none" stroke="#1E0846" stroke-width="3.5"/>
        <path d="M26 17 V27 H33" fill="none" stroke="#1E0846" stroke-width="3.5" stroke-linecap="round"/>
      </svg>
      <span>7:00pm - 10:00pm</span>
    </div>
  </div>

  <div class="venue">
    <span>At The Giggle Room</span>
    <span class="venue__dot"></span>
    <span>123 Anywhere St., Any City</span>
    <span class="venue__dot"></span>
    <span>Free Parking Area</span>
  </div>
</main>
</body>
</html>
```